Custom Software Company Needs a Direct Mail Postcard

We need a postcard or A5 sized mailer to be used in an unaddressed mail drop.
Headline: Warning
Subhead: Excel & Paper Considered Harmful For Business
Possible images: triangular warning logos
Breakout (possibly a sidebar):
Breakout Headline: Free Quotes
We come and discuss your requirements and provide a free, no obligation quote.
Main text:
- Are you juggling multiple systems that don't talk to each other?
- Are staff constantly updating or re-entering data?
- Do you worry that things will be missed?
- Do staff spend a lot of time doing the same thing over and over?
- Is finding information or reports challenging?
Custom software can bring all your information together in one place and automate all the repetitive tasks. With the information together, things are no longer missed and you can get the information you need, when you need it.
Whatever your requirements, we can build a system to suit. Visit our website or call us now for a free, no obligation quote.
Call 9377 5806
www.7 qo.com.au
Logo
Possible items to use on the postcard:
- Client logos
- Testimonials
- Picture of me
- Branding items on the website
Light industry manufacturers, heavy machinery hire, construction, occupational health and safety.
It Company

```html
<!DOCTYPE html>
<html lang="en">
<head>
<meta charset="utf-8">
<title>SevenQo Direct Mail Postcard</title>
<link rel="stylesheet" href="https://fonts.googleapis.com/css2?family=Roboto+Condensed:wght@400;700;800&display=swap">
<style>
  :root {
    --backdrop: #3d3d3d;
    --paper: #ffffff;
    --brand-red: #cf373a;
    --brand-blue: #0d4d92;
    --ink-blue: #0f4a8c;
    --photo-light: #dfe8ee;
    --photo-mid: #a9bccb;
  }
  * { margin: 0; padding: 0; box-sizing: border-box; }
  html, body { width: 1200px; height: 1000px; overflow: hidden; }
  body {
    background: var(--backdrop);
    font-family: "Roboto Condensed", "Arial Narrow", sans-serif;
    position: relative;
  }
  .postcard {
    position: absolute; left: 121px; top: 160px;
    width: 959px; height: 678px;
    background: var(--paper);
    overflow: hidden;
  }
  .postcard > * { position: absolute; }
  .headline {
    left: 48px; top: 30px;
    font-size: 106px; font-weight: 800; line-height: 1;
    color: var(--brand-red); letter-spacing: 0.5px;
  }
  .subhead {
    left: 471px; top: 48px; width: 488px; height: 76px;
    background: var(--brand-blue); color: #fff;
    font-size: 30px; font-weight: 700; line-height: 31px;
    padding: 8px 0 0 15px; text-transform: uppercase;
  }
  .questions { left: 34px; top: 158px; list-style: none; }
  .questions li {
    font-size: 16.5px; line-height: 25.2px; text-transform: uppercase;
    padding-left: 24px; position: relative;
  }
  .questions li::before {
    content: ""; position: absolute; left: 0; top: 6px;
    width: 13px; height: 13px; border-radius: 50%;
  }
  .questions .blue { color: var(--ink-blue); }
  .questions .blue::before { background: var(--brand-blue); }
  .questions .red { color: var(--brand-red); }
  .questions .red::before { background: var(--brand-red); }
  .solution {
    left: 0; top: 299px; width: 562px; height: 79px;
    background: var(--brand-red); color: #fff;
    font-size: 15.5px; line-height: 19px; padding: 11px 0 0 33px;
  }
  .contact { left: 48px; top: 393px; font-size: 26px; line-height: 29px; font-weight: 700; }
  .contact .label { color: var(--brand-red); font-weight: 400; }
  .contact .value { color: var(--ink-blue); }
  .hero-image {
    left: 569px; top: 152px; width: 390px; height: 466px;
    background: radial-gradient(ellipse at 60% 45%, var(--photo-light), #fff 75%);
  }
  .swooshes { left: 0; top: 0; width: 959px; height: 678px; }
  .quote-invite {
    left: 32px; top: 514px; font-size: 15.5px; line-height: 18px; color: #fff;
  }
  .quote-rule { left: 32px; top: 556px; width: 420px; height: 2px;
    background: linear-gradient(90deg, #fff, rgba(255,255,255,0)); }
  .free-quotes { left: 31px; top: 563px; color: #fff; }
  .free-quotes h2 { font-size: 46px; font-weight: 800; line-height: 46px; }
  .free-quotes p { font-size: 17.5px; line-height: 20px; text-transform: uppercase; }
  .brand { left: 634px; top: 555px; color: var(--ink-blue); }
  .brand-name { font-size: 52px; font-weight: 400; line-height: 56px; }
  .brand-tagline { font-size: 19px; line-height: 22px; }
  .brand-dot {
    left: 893px; top: 614px; width: 20px; height: 20px;
    border-radius: 50%; background: var(--brand-blue);
  }
</style>
</head>
<body>
  <main class="postcard">
    <div class="hero-image" role="img" aria-label="Photo of a hand drawing a network of connected people icons with a marker"></div>

    <svg class="swooshes" viewBox="0 0 959 678" aria-hidden="true">
      <polygon points="0,458 408,482 545,598 512,678 502,678 534,600 400,492 0,472" fill="var(--brand-red)"/>
      <polygon points="0,472 400,492 534,600 502,678 0,678" fill="var(--brand-blue)"/>
      <path d="M500 678 C540 565 600 548 700 530 L959 474 L959 500 L700 555 C625 570 565 600 514 678 Z" fill="var(--brand-red)"/>
    </svg>

    <h1 class="headline">WARNING</h1>
    <div class="subhead">Excel &amp; Paper Considered<br>Harmful for Business</div>

    <ul class="questions">
      <li class="blue">Are you juggling multiple systems that don't talk to each other?</li>
      <li class="red">Are staff constantly updating or re-entering data?</li>
      <li class="blue">Do you worry that things will be missed?</li>
      <li class="red">Do staff spend a lot of time doing the same thing over and over?</li>
      <li class="blue">Is finding information or reports challenging?</li>
    </ul>

    <p class="solution">Custom software can bring all your information together in one place and automate all the repetitive tasks. With the information together, things are no longer missed and you can get the information you need, when you need it.</p>

    <div class="contact">
      <div><span class="label">Call : </span><span class="value">9377 5806</span></div>
      <div><span class="label">Visit: </span><span class="value">www.7 qo.com.au</span></div>
    </div>

    <p class="quote-invite">Whatever your requirements, we can build a system to suit.<br>Visit our website or call us now for a free, no obligation quote.</p>
    <div class="quote-rule"></div>
    <div class="free-quotes">
      <h2>FREE QUOTES</h2>
      <p>We come and discuss your requirements<br>and provide a free, no obligation quote.</p>
    </div>

    <div class="brand">
      <div class="brand-name">SevenQo</div>
      <div class="brand-tagline">custom business software</div>
    </div>
    <div class="brand-dot"></div>
  </main>
</body>
</html>
```